Restaurant needs promotional material

We need a design for a "free welcome cocktail on your next visit" flyer. The flyer must have a black background and be contemporary. Our logo is the name of the restaurant which is "Amber Nook" in edwardian script font with italic selected.

There must be a section for terms and conditions, which are:
1 free cocktail for every main course ordered from our evening menu over the value of 9.95€ (not including taxes). The number of free cocktails cannot exceed the number of main courses ordered from your previous visit. This offer is only valid when you present both this flyer and your receipt from your previous visit. This offer does not include ice cream cocktails. This offer cannot be used in conjunction with any other offer or promotion. Limit 1 free cocktail per person. We reserve the right to final interpretation of this offer and can cancel the offer at any time.

A space must also be left where we can write a "valid until" date.

The uploaded photos are a picture of our cocktail menu and the publicity we are currently running, so you can get a feel for your design.

Thanks

Industry/Entity Type

Restaurant

Colors
000000

Requirements
Must have
• Also included in the flyer is the text " Please present this flyer along with your bill from your previous visit upon arrival.
• Pictures of cocktails!

```html
<!DOCTYPE html>
<html lang="en">
<head>
<meta charset="utf-8">
<title>Amber Nook – Free Welcome Cocktail Flyer</title>
<link rel="stylesheet" href="https://fonts.googleapis.com/css2?family=Great+Vibes&family=Dancing+Script:wght@600&family=Playfair+Display:wght@400&family=Archivo+Narrow:wght@400;500&display=swap">
<style>
  :root {
    --ink: #000000;
    --paper: #ffffff;
    --ghost: #2a2a2a;
    --magenta: #e01fc6;
    --ring: #6e1d82;
    --ring-glow: #a23cc0;
    --photo-dark: #1a0508;
    --photo-red: #5a0c14;
    --photo-amber: #8a4a12;
  }
  * { margin: 0; padding: 0; box-sizing: border-box; }
  html, body { width: 1200px; height: 2541px; overflow: hidden; background: var(--ink); }
  .flyer {
    position: relative; width: 1200px; height: 2541px; overflow: hidden;
    background: radial-gradient(ellipse at 50% 75%, #1c0a22 0%, var(--ink) 60%);
    color: var(--paper);
  }
  .backdrop-word {
    position: absolute; top: -40px; left: 0; width: 100%; text-align: center;
    font-family: "Playfair Display", serif; font-size: 170px; letter-spacing: 10px;
    color: var(--ghost); opacity: .55; white-space: nowrap;
  }
  .backdrop-sweep { position: absolute; inset: 0; }
  .brand { position: absolute; top: 110px; left: 0; width: 100%; text-align: center; }
  .brand-kicker {
    font-family: "Playfair Display", serif; font-size: 66px; letter-spacing: 4px;
    line-height: 1; margin-left: 40px;
  }
  .brand-name {
    font-family: "Great Vibes", cursive; font-size: 220px; line-height: .9; color: var(--paper);
    white-space: nowrap;
  }
  .notice-band {
    position: absolute; top: 480px; left: -50px; width: 1300px; height: 130px;
    background: var(--magenta); transform: rotate(-4deg);
    display: flex; flex-direction: column; justify-content: center; align-items: center;
    font-family: "Archivo Narrow", sans-serif; font-size: 40px; line-height: 1.1;
    text-transform: uppercase; text-align: center; letter-spacing: 1px; white-space: nowrap;
  }
  .cocktail-photo {
    position: absolute; top: 700px; left: 0; width: 1200px; height: 1010px;
    background:
      radial-gradient(ellipse at 20% 55%, var(--photo-amber) 0%, transparent 35%),
      radial-gradient(ellipse at 85% 60%, var(--photo-amber) 0%, transparent 30%),
      linear-gradient(180deg, var(--ink) 0%, var(--photo-dark) 25%, var(--photo-red) 55%, var(--ink) 100%);
  }
  .offer-ring { position: absolute; left: 600px; top: 1280px; width: 600px; height: 600px; }
  .offer {
    position: absolute; left: 590px; top: 1380px; width: 620px; text-align: center;
    white-space: nowrap;
  }
  .offer-free { font-family: "Great Vibes", cursive; font-size: 160px; line-height: 1; }
  .offer-line { font-family: "Dancing Script", cursive; font-weight: 600; font-size: 64px; line-height: 1.2; letter-spacing: 2px; }
  .offer-sub { font-family: "Dancing Script", cursive; font-weight: 600; font-size: 50px; line-height: 1.3; letter-spacing: 3px; }
  .terms { position: absolute; left: 10px; top: 1985px; width: 1180px; font-family: "Archivo Narrow", sans-serif; }
  .terms-title { font-size: 44px; font-weight: 500; letter-spacing: 2px; text-transform: uppercase; margin-bottom: 18px; }
  .terms-body { font-size: 31px; line-height: 50px; }
  .valid { position: absolute; left: 590px; top: 2450px; display: flex; align-items: center; gap: 26px; }
  .valid-label { font-family: "Archivo Narrow", sans-serif; font-size: 50px; text-transform: uppercase; }
  .valid-field { width: 320px; height: 70px; background: var(--paper); }
</style>
</head>
<body>
<main class="flyer">
  <div class="backdrop-word" aria-hidden="true">RESTAURANT</div>
  <svg class="backdrop-sweep" width="1200" height="2541" aria-hidden="true">
    <path d="M0 260 Q400 120 1200 60 L1200 110 Q500 180 0 330 Z" fill="#1a1a1a" opacity=".6"/>
    <path d="M0 620 Q500 560 1200 380 L1200 420 Q600 600 0 680 Z" fill="#161616" opacity=".6"/>
  </svg>

  <header class="brand">
    <div class="brand-kicker">RESTAURANT</div>
    <div class="brand-name">Amber Nook</div>
  </header>

  <div class="notice-band">
    <span>Please present this flyer along with your bill from</span>
    <span>your previous visit upon arrival</span>
  </div>

  <div class="cocktail-photo" role="img" aria-label="Photograph of a row of colourful cocktails in martini and tumbler glasses against a dark red curtain"></div>

  <svg class="offer-ring" viewBox="0 0 600 600" aria-hidden="true">
    <circle cx="300" cy="300" r="270" fill="none" stroke="var(--ring)" stroke-width="50"/>
    <circle cx="300" cy="300" r="245" fill="none" stroke="var(--ring-glow)" stroke-width="3" opacity=".6"/>
  </svg>

  <section class="offer">
    <div class="offer-free">Free</div>
    <div class="offer-line">welcome cocktail</div>
    <div class="offer-sub">on your next visit</div>
  </section>

  <section class="terms">
    <h2 class="terms-title">Terms and conditions:</h2>
    <p class="terms-body">Free cocktail for every main course ordered from our evening menu over the value of 9.95€ (not including taxes). ● The number of free cocktails cannot exceed the number of main courses ordered from your previous visit. ● This offer does not include ice cream cocktails. ● This offer cannot be used in conjunction with any other offer or promotion. ● Limit 1 free cocktail per person. ● We reserve the right to final interpretation of this offer and can cancel the offer at any time.</p>
  </section>

  <div class="valid">
    <span class="valid-label">Valid until:</span>
    <span class="valid-field"></span>
  </div>
</main>
</body>
</html>
```